Business Card design for a company called Tallow Flame NI

I need a business card design for my oil fired boiler servicing company. I have a logo design already and Im just looking that incorporated into the business card design. card details; Tallow Flame NI
Oil Burner Servicing - Mid Ulster Area
Service Engineer - Owen Marsh
Mobile 07751364927
email - Tallow.Flame.NI@hearthmail.example
www.tallowflameni.example
I carry out Servicing, Commissioning, Fault Finding, Warranty Validation
Target Market(s)
home owners with oil fired central heating
Industry/Entity Type
Business
Contact Information for Business Card
Tallow Flame NI
Tell. 07751364927
Web: www.tallowflameni.example
email Tallow.Flame.NI@Hearthmail.Example
Servicing Fault Finding Commissioning Warranty Validation
Look and feel

```html
<!DOCTYPE html>
<html lang="en">
<head>
<meta charset="utf-8">
<title>Tallow Flame NI – Business Card</title>
<link rel="stylesheet" href="https://fonts.googleapis.com/css2?family=Montserrat:wght@400;500;600;700&display=swap">
<style>
  :root {
    --backdrop: #e9e6e1;
    --green: #5cb947;
    --green-light: #7dc744;
    --green-dark: #45b04a;
    --ink: #6d6d6d;
    --rule: #d4d4d4;
    --paper: #ffffff;
  }
  * { margin: 0; padding: 0; box-sizing: border-box; }
  html, body { width: 1200px; height: 1000px; overflow: hidden; }
  body {
    background: var(--backdrop);
    font-family: "Montserrat", Arial, sans-serif;
    position: relative;
  }
  .card {
    position: absolute;
    left: 265px;
    width: 666px;
    overflow: hidden;
    box-shadow: 0 4px 14px rgba(0,0,0,0.18);
  }
  .card--front { top: 73px; height: 395px; background: var(--paper); }
  .card--back {
    top: 532px; height: 398px;
    background: radial-gradient(ellipse at 50% 45%, var(--green-light) 0%, var(--green) 55%, var(--green-dark) 100%);
  }

  .brand { position: absolute; display: flex; align-items: center; }
  .brand__dot { border-radius: 50%; flex: none; }
  .brand__name { font-weight: 600; line-height: 1; white-space: nowrap; }
  .brand__tagline {
    font-weight: 600; letter-spacing: 1.2px; text-transform: uppercase; white-space: nowrap;
  }

  .card--front .brand { right: 31px; top: 58px; }
  .card--front .brand__dot { width: 78px; height: 78px; background: var(--green); margin-right: 10px; }
  .card--front .brand__name { font-size: 33px; color: var(--green); }
  .card--front .brand__tagline { font-size: 9.5px; color: var(--green); margin-top: 9px; }

  .person { position: absolute; left: 33px; top: 195px; }
  .person__name { font-size: 21px; font-weight: 700; color: var(--green); letter-spacing: 0.3px; }
  .person__role { font-size: 16px; color: var(--ink); margin-top: 4px; }

  .divider { position: absolute; left: 33px; top: 263px; width: 452px; height: 1px; background: var(--rule); }

  .service { position: absolute; left: 33px; top: 284px; font-size: 16px; color: var(--ink); line-height: 24px; }
  .service__title { font-weight: 600; }

  .contacts { position: absolute; right: 30px; top: 250px; list-style: none; text-align: right; }
  .contacts li {
    display: flex; justify-content: flex-end; align-items: center;
    font-size: 16px; color: var(--ink); height: 27px; white-space: nowrap;
  }
  .contacts svg { width: 15px; height: 15px; margin-left: 8px; fill: var(--green); }

  .services-band {
    position: absolute; left: 0; bottom: 0; width: 100%; height: 28px;
    background: var(--green); color: #fff;
    font-size: 16px; letter-spacing: 2.4px; text-align: center; line-height: 28px; font-weight: 500;
    white-space: nowrap;
  }

  .card--back .brand { left: 50%; transform: translateX(-50%); top: 145px; }
  .card--back .brand__dot { width: 100px; height: 100px; background: #fff; margin-right: 15px; }
  .card--back .brand__name { font-size: 42px; color: #fff; }
  .card--back .brand__tagline { font-size: 12px; color: #fff; margin-top: 10px; }
  .back-url {
    position: absolute; left: 0; width: 100%; top: 348px;
    text-align: center; color: #fff; font-size: 16px; font-weight: 500;
  }
</style>
</head>
<body>
  <section class="card card--front">
    <div class="brand">
      <span class="brand__dot"></span>
      <div>
        <div class="brand__name">Tallow Flame NI</div>
        <div class="brand__tagline">Oil Burner Servicing - Mid Ulster Area</div>
      </div>
    </div>

    <div class="person">
      <div class="person__name">OWEN MARSH</div>
      <div class="person__role">Service Engineer</div>
    </div>

    <div class="divider"></div>

    <div class="service">
      <div class="service__title">Oil Burner Servicing</div>
      <div>Mid Ulster Area</div>
    </div>

    <ul class="contacts">
      <li>07751364927
        <svg viewBox="0 0 16 16" aria-hidden="true"><path d="M1 6c0-2 3-4 7-4s7 2 7 4v1h-4V5.5H5V7H1zM4 8h8l2 6H2z"/></svg>
      </li>
      <li>Tallow.Flame.NI@hearthmail.example
        <svg viewBox="0 0 16 16" aria-hidden="true"><path d="M1 3h14v10H1z"/><path d="M2 4l6 5 6-5" stroke="#fff" stroke-width="1.2" fill="none"/></svg>
      </li>
      <li>www.tallowflameni.example
        <svg viewBox="0 0 16 16" aria-hidden="true"><circle cx="7" cy="7" r="6"/><path d="M8 8l7 3-3 1-1 3z" stroke="#fff" stroke-width="0.8"/></svg>
      </li>
    </ul>

    <div class="services-band">Commissioning &nbsp;-&nbsp; Fault Finding &nbsp;-&nbsp; Warranty Validation</div>
  </section>

  <section class="card card--back">
    <div class="brand">
      <span class="brand__dot"></span>
      <div>
        <div class="brand__name">Tallow Flame NI</div>
        <div class="brand__tagline">Oil Burner Servicing - Mid Ulster Area</div>
      </div>
    </div>
    <div class="back-url">www.TallowFlameNI.example</div>
  </section>
</body>
</html>
```